Corvane Medical new year card

Hi,
I would like a New Year greetings card to send to my customers.

If you need to look at our logo : www.corvanemedical.com

If you want to play with images of our device, see
trelvacare.ca

The goal is to have a card to wish a happy new year and we look forward collaborating with them in the new year.

```html
<!DOCTYPE html>
<html lang="en">
<head>
<meta charset="utf-8">
<title>Corvane Medical – New Year Card</title>
<link rel="stylesheet" href="https://fonts.googleapis.com/css2?family=Oswald:wght@300;400&family=Great+Vibes&display=swap">
<style>
  :root {
    --paper: #ffffff;
    --gold: #c99a3e;
    --gold-light: #e8c777;
    --ink: #2a2a2a;
    --brand-grey: #5a5d63;
    --brand-accent: #e0622a;
  }
  * { margin: 0; padding: 0; box-sizing: border-box; }
  html, body { width: 848px; height: 1200px; overflow: hidden; background: var(--paper); }
  .card {
    position: relative;
    width: 848px;
    height: 1200px;
    background: var(--paper);
    font-family: "Oswald", "Arial Narrow", sans-serif;
  }
  .ornament-art {
    position: absolute;
    left: 40px;
    top: 0;
    width: 540px;
    height: 640px;
  }
  .brand {
    position: absolute;
    top: 62px;
    right: 44px;
    display: flex;
    align-items: center;
    gap: 12px;
  }
  .brand-mark {
    width: 26px;
    height: 26px;
    background: var(--brand-accent);
  }
  .brand-name {
    font-family: "Oswald", "Arial Narrow", sans-serif;
    font-weight: 400;
    font-size: 40px;
    line-height: 1;
    color: var(--brand-grey);
  }
  .greeting {
    position: absolute;
    right: 61px;
    top: 0;
    width: 700px;
    text-align: right;
  }
  .greeting-line {
    position: absolute;
    right: 0;
    font-weight: 300;
    font-size: 58px;
    line-height: 1;
    letter-spacing: 0.11em;
    margin-right: -0.11em;
    color: var(--gold);
    white-space: nowrap;
  }
  .greeting-line .dark { color: var(--ink); }
  .line-1 { top: 652px; }
  .line-2 { top: 727px; }
  .line-4 { top: 869px; }
  .line-5 { top: 944px; }
  .ampersand {
    position: absolute;
    right: 14px;
    top: 800px;
    font-family: "Great Vibes", cursive;
    font-size: 84px;
    line-height: 1;
    color: var(--gold);
  }
</style>
</head>
<body>
  <main class="card">
    <svg class="ornament-art" role="img" aria-label="Hanging gold and black Christmas baubles, stars and curled ribbons with scattered gold confetti" viewBox="0 0 540 640">
      <defs>
        <radialGradient id="ornamentGlow" cx="45%" cy="45%" r="60%">
          <stop offset="0%" stop-color="#e8c777" stop-opacity="0.75"/>
          <stop offset="55%" stop-color="#c99a3e" stop-opacity="0.35"/>
          <stop offset="100%" stop-color="#ffffff" stop-opacity="0"/>
        </radialGradient>
        <radialGradient id="ornamentShade" cx="40%" cy="75%" r="40%">
          <stop offset="0%" stop-color="#2a2a2a" stop-opacity="0.35"/>
          <stop offset="100%" stop-color="#2a2a2a" stop-opacity="0"/>
        </radialGradient>
      </defs>
      <rect width="540" height="640" fill="url(#ornamentGlow)"/>
      <rect width="540" height="640" fill="url(#ornamentShade)"/>
    </svg>

    <div class="brand">
      <span class="brand-mark"></span>
      <span class="brand-name">Corvane Medical</span>
    </div>

    <div class="greeting">
      <p class="greeting-line line-1">WE WISH YOU</p>
      <p class="greeting-line line-2">PEACEFUL HOLIDAYS</p>
      <span class="ampersand">&amp;</span>
      <p class="greeting-line line-4">A <span class="dark">SAFE</span> AND <span class="dark">HEALTHY</span></p>
      <p class="greeting-line line-5">NEW YEAR</p>
    </div>
  </main>
</body>
</html>
```